BUSINESS CARD - HALVERDINE RURAL SERVICES

I would like to create a business card for my fertilizer spreading business. I would like to incorporate my existing logo and also a description of the services offered. The business card will be given to farmers so must be kept simple but effective. It will also be left in stores so much also be eye catching in order to stand out from other cards.

Target Market(s)

FARMERS

Requirements
Must have
• FRONT OF CARD = EXISTING LOGO + "CUSTOMISED SPREADING" below the logo

REAR Of CARD = SERVICES OFFERED AND CONTACT DETAILS

- Bulk fertilizer including Lime, Gypsum, Manure & Compost
- Granular fertilizer including Single Super, Urea, Gran-am, & Custom Blends
- Modern equipment - Autosteer & Variable Rate Capable
- Friendly & Reliable Service
- Contact Gus: 0471 502 318
Nice to have
• utilize same color scheme as existing logo

```html
<!DOCTYPE html>
<html lang="en">
<head>
<meta charset="utf-8">
<title>Halverdine Rural Services – Business Card</title>
<link href="https://fonts.googleapis.com/css2?family=Open+Sans:wght@400;600;700&display=swap" rel="stylesheet">
<style>
  :root {
    --backdrop: #e4e4e4;
    --charcoal: #555555;
    --paper: #f4f4f4;
    --white: #ffffff;
    --orange: #ef8f1f;
    --text: #4f4f4f;
  }
  * { margin: 0; padding: 0; box-sizing: border-box; }
  html, body {
    width: 1200px; height: 960px; overflow: hidden;
    background: var(--backdrop);
    font-family: "Open Sans", Arial, sans-serif;
  }
  .canvas { position: relative; width: 1200px; height: 960px; }

  .card {
    position: absolute; left: 306px; width: 587px; height: 359px; overflow: hidden;
  }

  /* Front */
  .card-front { top: 101px; background: var(--charcoal); }
  .brand-mark {
    position: absolute; left: 233px; top: 75px;
    width: 122px; height: 122px; border-radius: 50%;
    background: var(--white);
  }
  .brand-name {
    position: absolute; left: 0; right: 0; top: 218px;
    text-align: center; color: var(--white);
    font-weight: 700; font-size: 33px; letter-spacing: -0.5px;
  }
  .tagline {
    position: absolute; left: 0; right: 0; top: 303px;
    text-align: center; color: var(--white);
    font-weight: 700; font-size: 18px; letter-spacing: 1.6px;
  }

  /* Back */
  .card-back { top: 504px; background: var(--paper); }
  .livestock-art {
    position: absolute; left: 0; bottom: 0; width: 310px; height: 175px;
    background: linear-gradient(180deg, #5e5e5e 0%, var(--charcoal) 100%);
    border-top-right-radius: 120px;
  }
  .contact-name {
    position: absolute; left: 92px; top: 96px;
    color: var(--orange); font-weight: 700; font-size: 36px; letter-spacing: 0.5px;
  }
  .contact-phone {
    position: absolute; left: 49px; top: 139px;
    display: flex; align-items: center; gap: 5px;
    color: var(--text); font-size: 22px;
  }
  .contact-phone svg { width: 24px; height: 24px; }

  .services {
    position: absolute; right: 20px; top: 44px; list-style: none;
    text-align: right; color: var(--text); font-size: 16px; line-height: 20.5px;
  }
  .service { margin-bottom: 12px; }
  .service-title { font-weight: 700; display: flex; justify-content: flex-end; align-items: center; gap: 8px; }
  .service-title::after {
    content: ""; width: 12px; height: 12px; border-radius: 50%; background: var(--orange);
  }
  .service-detail { margin-right: 20px; }
</style>
</head>
<body>
<main class="canvas">

  <section class="card card-front" aria-label="Card front">
    <div class="brand-mark" aria-hidden="true"></div>
    <h1 class="brand-name">Halverdine Rural Services</h1>
    <p class="tagline">CUSTOMISED SPREADING</p>
  </section>

  <section class="card card-back" aria-label="Card back">
    <div class="livestock-art" role="img" aria-label="Silhouettes of a cow and a sheep standing on grass"></div>

    <h2 class="contact-name">GUS</h2>
    <p class="contact-phone">
      <svg viewBox="0 0 24 24" aria-hidden="true">
        <circle cx="12" cy="12" r="10.5" fill="none" stroke="var(--orange)" stroke-width="1.6"/>
        <path d="M8.6 6.8l1.7 2.4-1 1.2c.7 1.6 1.9 2.8 3.4 3.5l1.2-1 2.4 1.7-.8 1.8c-4.2-.3-7.9-4-8.2-8.3z" fill="var(--orange)"/>
      </svg>
      0471 502 318
    </p>

    <ul class="services">
      <li class="service">
        <div class="service-title">Bulk Fertilizer</div>
        <div class="service-detail">including Lime, Gypsum,<br>Manure &amp; Compost</div>
      </li>
      <li class="service">
        <div class="service-title">Granular Fertilizer</div>
        <div class="service-detail">including Single Super,<br>Urea, Gran-am<br>&amp; Custom Blends</div>
      </li>
      <li class="service">
        <div class="service-title">Modern Equipment</div>
        <div class="service-detail">Autosteer &amp; Variable<br>Rate Capable</div>
      </li>
      <li class="service">
        <div class="service-title">Friendly &amp; Reliable Service</div>
      </li>
    </ul>
  </section>

</main>
</body>
</html>
```